Keys to business success

I love the principles of a book called "The quiet art of tending small gardens". I use the principles all the time at work. I'd like a poster made (map or web style design) to capture the books reminders. You can see a very basic verison of the design i'm looking for attached below "project summary".I've attached a word document of the text to include. Ive also attached two examples of the types of designs i'm looking for. The design will have to look modern and clear when printed on an 45.7 x 61 cm canvas.

Target Market(s)

Buisness people
Motivation

Industry/Entity Type

Business

Font styles to use
Serif

Requirements
Must have
• Web or map-like designs
• All 30 of the principles: 3 fonts (Title, sub-title and principles). The choice of fonts is up to the designer. No numbers for the principles.
• Professional feel
Nice to have
• Halos around phrases
Should not have
• No straight lines or ridgid concepts

```html
<!DOCTYPE html>
<html lang="en">
<head>
<meta charset="utf-8">
<title>30 Principles Of The Quiet Art Of Tending Small Gardens</title>
<link rel="stylesheet" href="https://fonts.googleapis.com/css2?family=Playfair+Display:wght@700;900&family=Libre+Baskerville:wght@700&family=Source+Serif+4:wght@400;600&display=swap">
<style>
  :root {
    --paper: #ffffff;
    --mist: #f3f5fb;
    --royal: #2a3cc0;
    --royal-soft: rgba(42,60,192,.22);
    --navy: #17207a;
    --orange: #f7941d;
    --orange-deep: #e2760c;
    --orange-soft: rgba(247,148,29,.30);
    --ink: #1e1f2a;
    --grey: #6d7080;
    --grey-soft: rgba(90,95,120,.20);
    --thread: #b8bfd8;
  }
  * { margin: 0; padding: 0; box-sizing: border-box; }
  html, body { width: 967px; height: 1200px; overflow: hidden; background: var(--paper); }
  .poster {
    position: relative; width: 967px; height: 1200px; overflow: hidden;
    background:
      radial-gradient(ellipse 520px 600px at 15% 70%, rgba(42,60,192,.07), rgba(42,60,192,0) 70%),
      radial-gradient(ellipse 520px 600px at 88% 72%, rgba(247,148,29,.10), rgba(247,148,29,0) 70%),
      var(--paper);
    font-family: "Source Serif 4", serif; color: var(--ink);
  }

  .web { position: absolute; left: 0; top: 0; width: 967px; height: 1200px; }

  .title {
    position: absolute; left: 46px; top: 44px;
    font-family: "Playfair Display", serif; font-weight: 900;
    font-size: 46px; line-height: 56px; color: var(--royal);
  }
  .title .accent { color: var(--orange); }

  .cluster { position: absolute; }
  .cluster-left { left: 30px; width: 420px; }
  .cluster-right { left: 520px; width: 430px; }
  .fundamentals { top: 318px; }
  .persuasion { top: 522px; }
  .liking { top: 318px; }
  .leadership { top: 660px; }

  .node-title {
    display: inline-block; margin-bottom: 12px;
    font-family: "Libre Baskerville", serif; font-weight: 700;
    font-size: 18px; line-height: 24px;
    padding: 9px 22px; border-radius: 30px;
  }
  .fundamentals .node-title { background: var(--royal); color: var(--orange); box-shadow: 0 0 0 6px var(--royal-soft), 0 0 22px 8px var(--royal-soft); }
  .liking .node-title { background: #eceef3; color: var(--ink); box-shadow: 0 0 0 6px var(--grey-soft), 0 0 22px 8px var(--grey-soft); }
  .persuasion .node-title { background: var(--paper); color: var(--navy); border: 2px solid var(--navy); box-shadow: 0 0 0 6px var(--royal-soft), 0 0 22px 8px var(--royal-soft); }
  .leadership .node-title { background: linear-gradient(180deg, var(--orange), var(--orange-deep)); color: #fff; font-size: 22px; letter-spacing: 1.5px; box-shadow: 0 0 0 6px var(--orange-soft), 0 0 22px 8px var(--orange-soft); }

  .principles { list-style: none; padding-left: 22px; display: flex; flex-direction: column; align-items: flex-start; gap: 7px; }
  .principles li {
    position: relative; background: var(--paper);
    font-size: 14.5px; line-height: 18px; padding: 5px 14px;
    border-radius: 16px;
  }
  .cluster-left .principles li { max-width: 398px; }
  .cluster-right .principles li { max-width: 408px; }
  .principles li::before {
    content: ""; position: absolute; left: -19px; top: 50%; margin-top: -5px;
    width: 10px; height: 10px; border-radius: 50%; border: 2px solid var(--paper);
  }
  .fundamentals li, .persuasion li { border: 1.5px solid rgba(42,60,192,.45); box-shadow: 0 0 12px 3px var(--royal-soft); }
  .fundamentals li::before, .persuasion li::before { background: var(--royal); }
  .liking li { border: 1.5px solid rgba(90,95,120,.40); box-shadow: 0 0 12px 3px var(--grey-soft); }
  .liking li::before { background: var(--grey); }
  .leadership li { border: 1.5px solid rgba(226,118,12,.55); box-shadow: 0 0 12px 3px var(--orange-soft); }
  .leadership li::before { background: var(--orange); }
</style>
</head>
<body>
<main class="poster">
  <svg class="web" viewBox="0 0 967 1200" aria-hidden="true">
    <defs>
      <radialGradient id="photo-tone" cx="55%" cy="40%" r="70%">
        <stop offset="0" stop-color="#ffd27a"/>
        <stop offset=".12" stop-color="#c9a76a"/>
        <stop offset=".35" stop-color="#6f86ad"/>
        <stop offset=".7" stop-color="#1f3660"/>
        <stop offset="1" stop-color="#0c1730"/>
      </radialGradient>
      <radialGradient id="hub-glow" cx="50%" cy="50%" r="50%">
        <stop offset="0" stop-color="#ffc766"/>
        <stop offset=".55" stop-color="#f7941d"/>
        <stop offset="1" stop-color="#f7941d" stop-opacity="0"/>
      </radialGradient>
    </defs>
    <path role="img" aria-label="Photograph of a hand touching a glowing network of people icons" d="M590 0 H967 V292 C880 318 760 296 682 240 C610 188 556 96 590 0 Z" fill="url(#photo-tone)"/>
    <g fill="none" stroke="var(--thread)" stroke-width="2" stroke-linecap="round">
      <path d="M470 640 C460 560 420 420 360 352"/>
      <path d="M470 640 C500 560 520 420 545 352"/>
      <path d="M470 640 C420 610 360 560 320 545"/>
      <path d="M470 640 C500 660 520 672 540 686"/>
      <path d="M620 240 C560 262 520 300 545 330"/>
      <path d="M38 390 C32 420 44 452 38 486"/>
      <path d="M38 580 C30 700 46 840 36 960 C32 1020 42 1060 38 1100"/>
      <path d="M528 374 C522 440 536 520 528 630"/>
      <path d="M528 718 C520 820 538 940 526 1040 C522 1090 532 1120 528 1140"/>
    </g>
    <circle cx="470" cy="640" r="40" fill="url(#hub-glow)" opacity=".55"/>
    <circle cx="470" cy="640" r="15" fill="var(--orange)" stroke="#fff" stroke-width="3"/>
  </svg>

  <h1 class="title">
    30 Principles<br>
    Of The <span class="accent">Quiet Art</span><br>
    Of Tending <span class="accent">Small</span><br>
    <span class="accent">Gardens</span>
  </h1>

  <section class="cluster cluster-left fundamentals">
    <h2 class="node-title">Fundamental Techniques in<br>Handling People</h2>
    <ul class="principles">
      <li>Don't Criticize, Condemn or Complain</li>
      <li>Give Honest, Sincere, Appreciation</li>
      <li>Arouse In The Other Person An Eager Want</li>
    </ul>
  </section>

  <section class="cluster cluster-left persuasion">
    <h2 class="node-title">Win People to Your Way of Thinking</h2>
    <ul class="principles">
      <li>The Only Way To Get The Best Of An Argument Is To Avoid It</li>
      <li>Show Respect For The Other Person's Opinion. Never Say, "You're Wrong."</li>
      <li>If You Are Wrong Admit It Quickly And Emphatically</li>
      <li>Begin In A Friendly Manner</li>
      <li>Get The Other Person Saying "Yes, Yes"</li>
      <li>Let The Other Person Do A Great Deal Of The Talking</li>
      <li>Let The Other Person Feel That The Idea Is His Or Hers</li>
      <li>Try Honestly To See Things From The Other Person's Point Of View</li>
      <li>Be Sympathetic With The Other Person's Ideas And Desires</li>
      <li>Appeal To The Nobler Motives</li>
      <li>Dramatize Your Ideas</li>
      <li>Throw Down A Challenge</li>
    </ul>
  </section>

  <section class="cluster cluster-right liking">
    <h2 class="node-title">Making People Like You</h2>
    <ul class="principles">
      <li>Become Genuinely Interested In Other People</li>
      <li>Smile</li>
      <li>A Person's Name Is To That Person The Sweetest And Most Important Sound</li>
      <li>Be A Good Listener. Encourage Others To Talk About Themselves</li>
      <li>Talk In Terms Of The Other Person's Interests</li>
      <li>Make The Other Person Feel Important - And Do It Sincerely</li>
    </ul>
  </section>

  <section class="cluster cluster-right leadership">
    <h2 class="node-title">BEING A LEADER</h2>
    <ul class="principles">
      <li>Begin With Praise And Honest Appreciation</li>
      <li>Call Attention To People's Mistakes Indirectly</li>
      <li>Talk About Your Own Mistakes Before Criticizing The Other Person</li>
      <li>Ask Questions Instead Of Giving Direct Orders</li>
      <li>Let The Other Person Save Face</li>
      <li>Praise The Slightest Improvement And Praise Every Improvement.</li>
      <li>Give The Other Person A Fine Reputation To Live Up To</li>
      <li>Use Encouragement. Make The Fault Seem Easy To Correct</li>
      <li>Make The Other Person Happy About Doing The Thing You Suggest</li>
    </ul>
  </section>
</main>
</body>
</html>
```